Gift voucher for a photo shoot, folding card DIN long (21 x 9.8 cm)

Hello, I'm a professional photographer and need a new design for my gift voucher card for a photo shoot. The design should be applicable to all types of photo shoots (neutral). I prefer a sophisticated design. The folded card should be printed on both sides.
My data should be included: Logo, Address: Wendtholzer Strße 27, 07549 Gera, Email: fotograf@malteburgardt.eu, Website: www.malteburgardt.eu Tel.: 0173 / 4958302
Updates

Please design the folding card in DIN long format (105 x 210 mm, landscape format). The card should open horizontally. Please design the front with the words "Gift voucher for you" and my logo. Please make the logo small – the words "Gift voucher" should be in the foreground.
The colors - use elegant gray with gold or white font color.
The inside should contain the words: Photo shoot for ........ worth .....€, as well as my logo.
My contact details should be on the back.

Target Market(s)

Private customer

Colors

Designer to choose only greyscale colors for use in the design.

Requirements
Must have
• Noble appearance, a gift voucher that one likes to give away, words: Gift voucher for you, photo shoot for ..., worth .......€
Nice to have
• Noble appearance of the gift voucher, a gift voucher that you like to give away
Should not have
• no pictures

```html
<!DOCTYPE html>
<html lang="de">
<head>
<meta charset="utf-8">
<title>Geschenkgutschein – Malte Burgardt Fotograf</title>
<link rel="stylesheet" href="https://fonts.googleapis.com/css2?family=Cinzel:wght@400;600&family=Montserrat:wght@400;500&display=swap">
<style>
  :root {
    --page-bg: #e5e6e8;
    --card-bg: #ffffff;
    --card-edge: #b9babc;
    --gold-dark: #c58a2c;
    --gold-light: #f0d48f;
    --gold-pale: #f3ebe0;
    --silver-dark: #9a9a9a;
    --silver-light: #dcdcdc;
    --text-grey: #b3b3b3;
    --label-grey: #a9a9a9;
    --ink: #1a1a1a;
    --ribbon: linear-gradient(90deg, #d9a04e 0%, #c58a2c 12%, #e0c3a0 35%, #f3ebe0 52%, #eed9a8 72%, #f0cd84 100%);
  }
  * { margin: 0; padding: 0; box-sizing: border-box; }
  html, body { width: 1079px; height: 1200px; overflow: hidden; background: var(--page-bg); }
  body { position: relative; font-family: "Montserrat", sans-serif; }

  .card {
    position: absolute; left: 143px; width: 793px; height: 396px;
    background: var(--card-bg); border: 1px solid var(--card-edge); overflow: hidden;
  }
  .card--front { top: 137px; }
  .card--inside { top: 652px; }

  .ribbon { position: absolute; }
  .ribbon--horizontal { left: 0; right: 0; height: 11px; background: var(--ribbon); }
  .card--front .ribbon--horizontal { top: 148px; }
  .card--inside .ribbon--horizontal { top: 225px; }
  .ribbon--vertical {
    top: 0; bottom: 0; left: 391px; width: 11px;
    background: linear-gradient(180deg, #f0cd84 0%, #f3ebe0 40%, #e0c3a0 70%, #c58a2c 100%);
  }
  .bow {
    position: absolute; left: 346px; top: 128px; width: 100px; height: 80px;
    border-radius: 45% 45% 30% 30%;
    background: radial-gradient(ellipse at 50% 30%, #f3e6d6 0%, #e6cfb0 60%, rgba(230,207,176,0) 100%);
  }

  .brand { position: absolute; text-align: center; font-family: "Cinzel", serif; color: var(--ink); }
  .brand__mark {
    display: block; margin: 0 auto 6px; width: 38px; height: 38px;
    border: 1.5px solid var(--ink); border-radius: 50%;
  }
  .brand__name { display: block; font-size: 17px; font-weight: 400; letter-spacing: 0.5px; line-height: 1; }
  .brand__tagline { display: block; font-size: 7px; letter-spacing: 3px; margin-top: 3px; }
  .card--front .brand { left: 509px; width: 200px; top: 34px; }
  .card--inside .brand { left: 296px; width: 200px; top: 230px; }

  .voucher-title {
    position: absolute; left: 452px; width: 290px; top: 176px; text-align: center;
    font-family: "Cinzel", serif; font-weight: 600; font-size: 41px; line-height: 43px;
  }
  .voucher-title span {
    background: linear-gradient(90deg, var(--silver-dark), var(--silver-light) 60%, var(--silver-dark));
    -webkit-background-clip: text; background-clip: text; color: transparent;
  }
  .voucher-title .voucher-title__accent {
    background: linear-gradient(90deg, var(--gold-dark), var(--gold-light));
    -webkit-background-clip: text; background-clip: text; color: transparent;
  }
  .title-rule {
    position: absolute; left: 462px; width: 270px; top: 341px; height: 1px; background: #e8cf9f;
  }
  .website {
    position: absolute; left: 462px; width: 270px; top: 369px; text-align: center;
    font-size: 11px; letter-spacing: 1.6px; color: var(--text-grey);
  }

  .contact { position: absolute; right: 426px; top: 311px; list-style: none; }
  .contact li {
    display: flex; align-items: center; justify-content: flex-end; gap: 8px;
    font-size: 13.5px; line-height: 21px; color: var(--text-grey);
  }
  .contact svg { width: 14px; height: 14px; flex: none; }

  .voucher-field {
    position: absolute; left: 53px; right: 51px; display: flex; align-items: baseline;
    font-family: "Cinzel", serif; font-weight: 600; font-size: 15px; color: var(--label-grey);
  }
  .voucher-field__dots { flex: 1; margin-left: 6px; border-bottom: 2px dotted #c4c4c4; height: 1px; }
  .voucher-field--subject { top: 76px; }
  .voucher-field--value { top: 135px; }
</style>
</head>
<body>

<section class="card card--front">
  <div class="ribbon ribbon--horizontal"></div>
  <div class="ribbon ribbon--vertical"></div>
  <div class="bow" role="img" aria-label="Goldene Geschenkschleife"></div>

  <div class="brand">
    <span class="brand__mark"></span>
    <span class="brand__name">Malte Burgardt</span>
    <span class="brand__tagline">FOTOGRAF</span>
  </div>

  <h1 class="voucher-title">
    <span>Geschenk</span><br>
    <span>Gutschein</span><br>
    <span class="voucher-title__accent">für</span> <span>Dich</span>
  </h1>
  <div class="title-rule"></div>
  <p class="website">www.malteburgardt.eu</p>

  <ul class="contact">
    <li>0173 / 4958302
      <svg viewBox="0 0 14 14" aria-hidden="true"><rect x="3.5" y="1" width="7" height="12" rx="1.3" fill="none" stroke="#d9a04e" stroke-width="1.3"/><line x1="6" y1="11" x2="8" y2="11" stroke="#d9a04e" stroke-width="1.2"/></svg>
    </li>
    <li>Wendtholzer Strße 27, 07549 Gera
      <svg viewBox="0 0 14 14" aria-hidden="true"><path d="M7 13 C4 9 2.5 7 2.5 5 a4.5 4.5 0 0 1 9 0 c0 2 -1.5 4 -4.5 8z" fill="none" stroke="#e0b86a" stroke-width="1.2"/><circle cx="7" cy="5" r="1.5" fill="none" stroke="#e0b86a" stroke-width="1.1"/></svg>
    </li>
    <li>fotograf@malteburgardt.eu,
      <svg viewBox="0 0 14 14" aria-hidden="true"><rect x="1" y="2.5" width="12" height="9" rx="1" fill="none" stroke="#d9a04e" stroke-width="1.3"/><path d="M1.5 3.5 L7 8 L12.5 3.5" fill="none" stroke="#d9a04e" stroke-width="1.3"/></svg>
    </li>
  </ul>
</section>

<section class="card card--inside">
  <div class="voucher-field voucher-field--subject">Fotoshooting für<span class="voucher-field__dots"></span></div>
  <div class="voucher-field voucher-field--value">im Wert von<span class="voucher-field__dots"></span>€</div>
  <div class="ribbon ribbon--horizontal"></div>
  <div class="brand">
    <span class="brand__mark"></span>
    <span class="brand__name">Malte Burgardt</span>
    <span class="brand__tagline">FOTOGRAF</span>
  </div>
</section>

</body>
</html>
```